Design some Business Cards for Kelvo Systems

I need a design for business cards. I have an existing logo.

I am a sole trader (work for myself) and I provide computer and IT technology support services to small businesses in Australia. I advise business owners on how to best use and manage their IT systems and computers and I provide onsite computer troubleshooting services.
The style should reflect the professional nature of my work.
I would likely favour a simpler and clean design.

The artwork needs to be:
Single sided (just the front of the card)
89mm x 54mm in size.
Full colour.
To be printed on white stock (paper)

Details that need to be included on the business cards are:
Logo
Name Miles BBBBBBBB
Email address miles@kelvosys.example
Phone number 2222 222 222

The exact details will be supplied at the end of the contest for the final artwork.
Final artwork would need to be print ready – I can provide examples of what they need to look like.

```html
<!DOCTYPE html>
<html lang="en">
<head>
<meta charset="utf-8">
<title>Kelvo Systems – Business Card</title>
<link rel="stylesheet" href="https://fonts.googleapis.com/css2?family=Encode+Sans+Condensed:wght@300;400;500&display=swap">
<style>
  :root {
    --backdrop: #d3e0e4;
    --card: #ffffff;
    --brand-blue: #2b8ccf;
    --contact-panel: #7c7d7f;
    --contact-text: #ffffff;
    --mark-shadow: rgba(0, 0, 0, 0.12);
  }
  html, body {
    margin: 0;
    padding: 0;
    width: 1194px;
    height: 1200px;
    overflow: hidden;
    background: var(--backdrop);
  }
  .canvas {
    position: relative;
    width: 1194px;
    height: 1200px;
  }
  .business-card {
    position: absolute;
    left: 185px;
    top: 338px;
    width: 842px;
    height: 527px;
    background: var(--card);
    font-family: "Encode Sans Condensed", "Arial Narrow", sans-serif;
  }
  .brand {
    position: absolute;
    left: 70px;
    top: 68px;
    display: flex;
    align-items: center;
    gap: 26px;
  }
  .brand-mark {
    width: 100px;
    height: 100px;
    border-radius: 50%;
    background: var(--brand-blue);
  }
  .brand-name {
    margin: 0;
    font-size: 56px;
    font-weight: 400;
    color: var(--brand-blue);
    letter-spacing: -0.5px;
    line-height: 1;
  }
  .holder {
    position: absolute;
    left: 66px;
    top: 370px;
  }
  .holder-name {
    margin: 0;
    font-size: 38px;
    font-weight: 400;
    color: var(--brand-blue);
    line-height: 1;
  }
  .holder-role {
    margin: 16px 0 0;
    font-size: 26px;
    font-weight: 400;
    color: var(--brand-blue);
    line-height: 1;
  }
  .contact-panel {
    position: absolute;
    right: 0;
    top: 346px;
    width: 340px;
    height: 125px;
    background: var(--contact-panel);
    box-sizing: border-box;
    padding: 12px 42px 0 0;
    text-align: right;
    color: var(--contact-text);
    font-size: 26px;
    font-weight: 300;
    line-height: 38px;
  }
  .contact-panel p {
    margin: 0;
  }
</style>
</head>
<body>
  <main class="canvas">
    <section class="business-card" aria-label="Kelvo Systems business card">
      <header class="brand">
        <span class="brand-mark" aria-hidden="true"></span>
        <h1 class="brand-name">Kelvo Systems</h1>
      </header>

      <div class="holder">
        <h2 class="holder-name">Miles BBBBBBBB</h2>
        <p class="holder-role">Designation</p>
      </div>

      <address class="contact-panel">
        <p class="contact-email">miles@kelvosys.example</p>
        <p class="contact-phone">2222 222 222</p>
        <p class="contact-web">www.kelvosys.example</p>
      </address>
    </section>
  </main>
</body>
</html>
```